QRN Law Letterhead

Want law firm letterhead - both in terms of a pdf file that I can use electronically as letterhead by adding it as a background - and in terms of a file that I can send to a company to create actual letterhead.
Industry/Entity Type
Law Firm
Font styles to use
Sans Serif
Requirements
Must have
- Should have the following information (you can decide where to place):
- My name - Emil Vostrakian
- My email - emil@qrnlegalgroup.example
- My address - 2861 Corvella Parkway 318-742
- San Jose, California 95342
- Website - www.qrnlegalgroup.example
- Phone - 408-297-1586
- Fax - 408-853-2941
- The logo I attached
Nice to have
- I think I would prefer to have a black and white color scheme.
- I don't necessarily need a title after my name, but I have seen a few design submissions that include a generic title. The title I would use is "IP Litigator & Trademark Attorney"

```html
<!DOCTYPE html>
<html lang="en">
<head>
<meta charset="utf-8">
<title>QRN Law Letterhead</title>
<link href="https://fonts.googleapis.com/css2?family=Archivo+Black&family=Roboto:wght@400;700&display=swap" rel="stylesheet">
<style>
  :root {
    --ink: #000000;
    --paper: #ffffff;
    --text: #1a1a1a;
    --muted: #333333;
    --watermark: #f0f0f0;
    --rule-mid: #8a8a8a;
    --rule-edge: #ffffff;
  }
  html, body {
    margin: 0;
    padding: 0;
    width: 927px;
    height: 1200px;
    overflow: hidden;
    background: var(--paper);
  }
  .letterhead {
    position: relative;
    width: 927px;
    height: 1200px;
    background: var(--paper);
    font-family: "Roboto", Arial, sans-serif;
    color: var(--text);
  }
  .brand {
    position: absolute;
    top: 22px;
    left: 0;
    width: 100%;
    display: flex;
    justify-content: center;
    align-items: center;
    gap: 18px;
  }
  .brand-dot {
    width: 58px;
    height: 58px;
    border-radius: 50%;
    background: var(--ink);
  }
  .brand-name {
    font-family: "Roboto", Arial, sans-serif;
    font-weight: 700;
    font-size: 70px;
    line-height: 1;
    color: var(--ink);
    letter-spacing: 1px;
  }
  .title-bar {
    position: absolute;
    top: 160px;
    left: 82px;
    width: 763px;
    height: 54px;
    background: var(--ink);
    border-radius: 14px;
    display: flex;
    align-items: center;
    justify-content: center;
  }
  .title-bar h2 {
    margin: 0;
    font-family: "Archivo Black", Arial, sans-serif;
    font-weight: 400;
    font-size: 31px;
    color: var(--paper);
    letter-spacing: 0.5px;
  }
  .watermark {
    position: absolute;
    top: 560px;
    left: 0;
    width: 100%;
    text-align: center;
    font-family: "Roboto", Arial, sans-serif;
    font-weight: 700;
    font-size: 170px;
    line-height: 1;
    color: var(--watermark);
    user-select: none;
  }
  .footer-rule {
    position: absolute;
    top: 1095px;
    left: 40px;
    width: 847px;
    height: 2px;
    background: linear-gradient(to right, var(--rule-edge), var(--rule-mid) 50%, var(--rule-edge));
  }
  .contact {
    position: absolute;
    top: 1106px;
    left: 0;
    width: 100%;
    text-align: center;
  }
  .contact-name {
    margin: 0;
    font-weight: 700;
    font-size: 15px;
    line-height: 19px;
    color: var(--text);
  }
  .contact-address {
    margin: 0;
    font-size: 13px;
    line-height: 19px;
    color: var(--muted);
    letter-spacing: 0.3px;
  }
  .contact-lines {
    margin: 0;
    font-size: 13px;
    line-height: 19px;
    color: var(--muted);
  }
  .contact-lines strong { color: var(--text); font-weight: 700; }
  .base-band {
    position: absolute;
    left: 0;
    bottom: 0;
    width: 100%;
    height: 28px;
    background: var(--ink);
  }
</style>
</head>
<body>
  <div class="letterhead">
    <header class="brand">
      <span class="brand-dot" aria-hidden="true"></span>
      <h1 class="brand-name" style="margin:0;">QRN Law</h1>
    </header>

    <div class="title-bar">
      <h2>IP LITIGATOR &amp; TRADEMARK ATTORNEY</h2>
    </div>

    <div class="watermark" aria-hidden="true">QRN Law</div>

    <div class="footer-rule"></div>

    <footer class="contact">
      <p class="contact-name">Emil Vostrakian</p>
      <p class="contact-address">2861 Corvella Parkway 318-742, San Jose, California 95342</p>
      <p class="contact-lines"><strong>www.qrnlegalgroup.example</strong> | <strong>emil@qrnlegalgroup.example</strong> | Phone - <strong>408-297-1586</strong> | Fax - <strong>408-853-2941</strong></p>
    </footer>

    <div class="base-band"></div>
  </div>
</body>
</html>
```